food delivery web site design

Currently we have a smartphone app (ios/android) that is being used by our clients to make orders to about 30 different restaurants.

We would like to extent this and have also a website that is able to mimic the same functionalities:
- register
- show restaurants based on the selected address
- make order to an restaurant
- being able to process orders for other registered users (please read the attached doc for complete info on this)

Take a look at the attached doc for more info.

Android

```html
<!DOCTYPE html>
<html lang="ro">
<head>
<meta charset="utf-8">
<title>DineDash – Adaugă/Editează adresa</title>
<link rel="stylesheet" href="https://fonts.googleapis.com/css2?family=Bebas+Neue&family=Open+Sans:wght@400;600&display=swap">
<style>
  :root {
    --brand-red: #a3190b;
    --brand-red-dark: #7c1207;
    --shield: #2a2220;
    --footer: #2b2523;
    --accent-yellow: #f3c04a;
    --title-grey: #c6c6c6;
    --label: #555555;
    --text: #5a5a5a;
    --ink: #222222;
    --field-border: #d4d4d4;
    --rule: #cfcfcf;
    --button-grey: #6a6a6a;
    --doodle-bg: #f1f1f1;
    --white: #ffffff;
  }
  * { box-sizing: border-box; margin: 0; padding: 0; }
  html, body { width: 1200px; height: 1200px; overflow: hidden; background: var(--white); }
  .page {
    position: relative; width: 1300px; height: 1300px;
    transform: scale(0.923077); transform-origin: 0 0;
    font-family: "Open Sans", sans-serif; color: var(--text);
  }
  .display { font-family: "Bebas Neue", sans-serif; font-weight: 400; letter-spacing: 0.2px; }
  .abs { position: absolute; }

  /* header */
  .doodle-band { position: absolute; left: 0; top: 0; width: 1300px; height: 56px;
    background: linear-gradient(180deg, #f6f6f6, var(--doodle-bg)); }
  .header-bar { position: absolute; left: 0; top: 54px; width: 1300px; height: 60px;
    background: var(--brand-red); border-top: 2px solid var(--brand-red-dark); border-bottom: 2px solid var(--brand-red-dark); }
  .header-rule { position: absolute; top: 29px; height: 1px; background: rgba(255,255,255,0.75); }
  .call { position: absolute; left: 379px; top: 12px; color: var(--white); font-size: 31px; display: flex; align-items: center; gap: 4px; }
  .call .phone { color: var(--accent-yellow); display: flex; align-items: center; gap: 3px; }
  .dotted { position: absolute; left: 660px; top: 29px; width: 300px; border-top: 2px dotted rgba(243,192,74,0.7); }
  .auth { position: absolute; top: 17px; color: var(--white); font-size: 20px; display: flex; align-items: center; gap: 6px; }
  .brand-shield { position: absolute; left: 150px; top: 0; width: 172px; height: 172px; }
  .brand-name { position: absolute; left: 176px; top: 24px; width: 120px; height: 120px; border-radius: 50%;
    background: var(--white); display: flex; align-items: center; justify-content: center;
    color: var(--brand-red); font-size: 32px; box-shadow: inset 0 -6px 10px rgba(0,0,0,0.08); }

  /* title */
  .page-title { position: absolute; left: 152px; top: 252px; font-size: 64px; color: var(--title-grey); line-height: 1; }
  .title-rule { position: absolute; left: 150px; top: 321px; width: 1000px; height: 1px; background: var(--rule); }

  /* form */
  .label { position: absolute; font-size: 24px; color: var(--label); line-height: 1; }
  .field { position: absolute; border: 1px solid var(--field-border); background: var(--white); height: 40px; }

  /* saved addresses */
  .saved-title { position: absolute; left: 720px; top: 366px; font-size: 25px; color: #444; line-height: 1; }
  .saved-rule { position: absolute; left: 720px; top: 395px; width: 340px; height: 1px; background: var(--rule); }
  .address { position: absolute; left: 720px; width: 320px; font-size: 14px; line-height: 18px; color: var(--text); }
  .address b { font-weight: 600; }
  .actions { position: absolute; left: 719px; font-size: 18px; display: flex; gap: 19px; line-height: 1; }
  .actions .edit { color: var(--ink); }
  .actions .delete { color: var(--brand-red); }
  .separator { position: absolute; left: 720px; width: 338px; border-top: 1px dotted #b8b8b8; }

  /* buttons */
  .btn { position: absolute; top: 1079px; height: 45px; color: var(--white); font-size: 24px;
    display: flex; align-items: center; justify-content: center; }
  .btn-save { left: 150px; width: 178px; background: var(--brand-red); }
  .btn-cancel { left: 348px; width: 116px; background: var(--button-grey); }

  /* footer */
  .footer { position: absolute; left: 0; top: 1240px; width: 1300px; height: 60px;
    background: radial-gradient(circle at 50% 50%, #332c29, var(--footer)); color: #e6e6e6; font-size: 13px; }
  .footer-links { position: absolute; left: 149px; top: 21px; display: flex; }
  .footer-links span { padding: 0 10px; border-left: 1px solid #5a514d; }
  .footer-links span:first-child { padding-left: 0; border-left: none; }
  .copyright { position: absolute; right: 151px; top: 21px; }
</style>
</head>
<body>
<div class="page">
  <header>
    <div class="doodle-band" role="img" aria-label="Fundal decorativ cu desene de alimente și ustensile de bucătărie"></div>
    <div class="header-bar">
      <div class="header-rule" style="left:320px;width:40px"></div>
      <div class="header-rule" style="left:1152px;width:148px"></div>
      <div class="call display">
        <span>SUNĂ-NE LA</span>
        <span class="phone">
          <svg width="18" height="22" viewBox="0 0 18 22"><path d="M4 1 L8 5 L6 8 Q8 13 12 16 L15 14 L18 18 L15 21 Q8 21 3 12 Q0 5 4 1Z" fill="#f3c04a"/></svg>
          0700 123 456
        </span>
      </div>
      <div class="dotted"></div>
      <div class="auth display" style="left:982px">
        <svg width="15" height="14" viewBox="0 0 15 14"><path d="M1 13 Q1 5 9 5 L9 1 L15 7 L9 13 L9 9 Q4 9 1 13Z" fill="#fff"/></svg>
        LOGIN
      </div>
      <div class="auth display" style="left:1063px">
        <svg width="17" height="14" viewBox="0 0 17 14"><circle cx="6" cy="4" r="3.5" fill="#fff"/><path d="M0 14 Q0 8 6 8 Q12 8 12 14Z" fill="#fff"/><path d="M13 1 V7 M10 4 H16" stroke="#fff" stroke-width="2"/></svg>
        SIGN IN
      </div>
    </div>
    <svg class="brand-shield" viewBox="0 0 172 172">
      <polygon points="0,0 172,0 172,140 140,170 32,170 0,140" fill="#1e1816"/>
      <polygon points="4,0 168,0 168,138 138,166 34,166 4,138" fill="var(--shield)"/>
    </svg>
    <div class="brand-name display">DineDash</div>
  </header>

  <main>
    <h1 class="page-title display">ADAUGĂ/EDITEAZĂ ADRESA</h1>
    <div class="title-rule"></div>

    <form class="address-form">
      <span class="label display" style="left:149px;top:366px">ORAȘ</span>
      <div class="field" style="left:150px;top:396px;width:190px"></div>

      <span class="label display" style="left:149px;top:466px">STRADĂ</span>
      <div class="field" style="left:150px;top:496px;width:270px"></div>
      <span class="label display" style="left:439px;top:505px">NR.</span>
      <div class="field" style="left:470px;top:496px;width:60px"></div>

      <span class="label display" style="left:149px;top:566px">BLOC</span>
      <div class="field" style="left:150px;top:596px;width:110px"></div>
      <span class="label display" style="left:289px;top:605px">SCARĂ</span>
      <div class="field" style="left:350px;top:596px;width:110px"></div>

      <span class="label display" style="left:149px;top:666px">NR. APARTAMENT</span>
      <div class="field" style="left:150px;top:696px;width:65px"></div>

      <span class="label display" style="left:149px;top:766px">ALTE INFORMAȚII</span>
      <div class="field" style="left:150px;top:796px;width:330px;height:100px"></div>

      <span class="label display" style="left:149px;top:926px">NUME ADRESĂ</span>
      <div class="field" style="left:150px;top:956px;width:190px"></div>

      <div class="btn btn-save display">SALVEAZĂ ADRESA</div>
      <div class="btn btn-cancel display">ANULEAZĂ</div>
    </form>

    <section class="saved-addresses">
      <h2 class="saved-title display">3 ADRESE SALVATE</h2>
      <div class="saved-rule"></div>

      <p class="address" style="top:413px"><b>1.</b> Lorem ipsum dolor sit amet, consectetur adipiscing elit</p>
      <div class="actions display" style="top:465px"><span class="edit">EDITEAZĂ</span><span class="delete">ȘTERGE</span></div>
      <div class="separator" style="top:496px"></div>

      <p class="address" style="top:513px"><b>2.</b> Illum mallem levares, quo optimum atque humanissimum virum</p>
      <div class="actions display" style="top:565px"><span class="edit">EDITEAZĂ</span><span class="delete">ȘTERGE</span></div>
      <div class="separator" style="top:596px"></div>

      <p class="address" style="top:613px"><b>3.</b> Ab hoc autem quaedam non melius quam veteres, quaedam omnino relicta</p>
      <div class="actions display" style="top:665px"><span class="edit">EDITEAZĂ</span><span class="delete">ȘTERGE</span></div>
    </section>
  </main>

  <footer class="footer" role="img" aria-label="Subsol cu fundal decorativ închis cu desene de alimente">
    <nav class="footer-links">
      <span>Contactează-ne</span><span>Despre noi</span><span>Partenerii noștri</span><span>FAQ</span><span>Devino partener</span>
    </nav>
    <div class="copyright">Copyright © 2013 dinedash.ro. Toate drepturile rezervate.</div>
  </footer>
</div>
</body>
</html>
```